Burrow Chair

A5 Double Sided card for Chair Marketing
This will be our major marketing piece on a stiff piece fo cardboard
Dont feel the need to use all the words below "a picture tells the story" we can trim the words and make sure the message gets out
High end project
Feel free to use the word "burrow Chair" innovatively to give it some identity
Want it professional and you can use any of the photos as you see fit
mix up the words etc
• Upholstered in Italian Leather
• High Quality Merino Wool Sheepskins .
• 360 Degree rotation
• Handmade with love and detail
• Cosy
• Calming and unbelievably quiet acoustics
• Unique
This chair is unique and a labor of love and attention to detail, it’s a conversation starter or statement piece. It’s something you just can’t find anywhere.
The acoustics let you escape in any room whether you want to read a book or simply relax
The Dome or Halo chair
When Tapio Lindqvist had the first idea for the Dome Chair
in 1963, fibreglass was a relatively new material as glass reinforced products were not Batch Produced as they are today. The only possibility was to craft the chair with his own hands. It took Tapio and his brother in law nearly one year until the first prototype was ready.
The prototype was a success, it is still standing in Tapios house. By coincidence two young product managers from the company VELNO discovered the Dome Chair when visiting Tapio in order to look at some pine wood chairs. They immediately realised the potential of this design icon.
In 1966 for the first time the chair was presented at the Northern Interiors Expo in Cologne. Celebrities bought copies of the original for their homes and it found itself in a variety of Design Museums throughout the world.
The design of the chair was not only striking to look at but it was also comfortable and relaxing to sit in for long periods of time. The chair has been described as ''a room within a room''. It offers shelter, a calming atmosphere and privacy for the seated person.
Our Replica Tapio Lindqvist Dome chair is made to exacting standards. The shell is made from solid fiberglass, and is finished in Italian leather. The interior of the ball is padded and covered in lambswool merino sheepskins. The chair is available in different colours.
Feel free to photo shop the chair in front of a lifestyle scene ie an ope fireplace or modern room for a dynamic feel on the front side of the card
Contact details
Tie in the logo loaded as well
We are a small Australian Family creating unique products
TRV
Property of TRV Exports we love to create comfortable and unique things which people talk about and want to adorn their living spaces with.
We hope you love this product as much as we do and have many years enjoyment in it
Please order on our web site www.trvexports-example.com.au or email sales@trvexp-example.com.au
Mira Doyle
Marketing and Sales Manager
0491 203 417
Melbourne, Australia
Niche Market , for private and hotels and high end businesses

```html
<!DOCTYPE html>
<html lang="en">
<head>
<meta charset="utf-8">
<title>Burrow Chair – A5 Double Sided Card</title>
<link rel="stylesheet" href="https://fonts.googleapis.com/css2?family=Montserrat:wght@300;400;500;600;700&display=swap">
<style>
  :root {
    --stage: #d9d9d9;
    --slate: #4b5159;
    --slate-deep: #3d4249;
    --gold: #f2c21b;
    --gold-line: #e0b12a;
    --ink: #222428;
    --body: #55585e;
    --paper: #ffffff;
    --room-a: #5d6c84;
    --room-b: #a9b2c0;
  }
  * { box-sizing: border-box; margin: 0; padding: 0; }
  html, body { width: 1200px; height: 960px; overflow: hidden; }
  body {
    background: var(--stage);
    font-family: "Montserrat", sans-serif;
    position: relative;
  }
  .card {
    position: absolute;
    top: 112px;
    width: 520px;
    height: 736px;
    overflow: hidden;
    box-shadow: 0 6px 20px rgba(0,0,0,.18);
  }
  .card--front { left: 60px; background: linear-gradient(160deg, var(--slate) 0%, var(--slate-deep) 100%); }
  .card--back { left: 620px; background: var(--paper); }

  /* front */
  .front-photo {
    position: absolute; right: 0; top: 0; width: 200px; height: 230px;
    background: radial-gradient(ellipse at 55% 60%, #8a6a4c 0%, #c9b190 40%, #5c626a 75%);
  }
  .tagline {
    position: absolute; white-space: nowrap;
    font-size: 9px; letter-spacing: .08em; color: #fff; font-weight: 300;
  }
  .tagline b { font-weight: 600; }
  .card--front .tagline { left: 250px; top: 58px; }
  .title-box {
    position: absolute; border: 2px solid var(--gold); color: #fff;
    font-weight: 400; letter-spacing: .06em; text-transform: uppercase;
    padding: 6px 14px; white-space: nowrap;
  }
  .card--front .title-box { left: 34px; top: 120px; font-size: 26px; }
  .front-intro {
    position: absolute; left: 34px; top: 192px; width: 270px;
    color: #e4e6e9; font-size: 10px; line-height: 1.5; font-weight: 300;
  }
  .front-intro p + p { margin-top: 8px; }
  .feature-list {
    position: absolute; left: 34px; top: 306px; list-style: none;
    color: #fff; font-size: 11px; font-weight: 400; text-transform: uppercase; line-height: 1.3;
  }
  .feature-list li { margin-bottom: 9px; padding-left: 16px; position: relative; }
  .feature-list li::before {
    content: ""; position: absolute; left: 0; top: 4px; width: 6px; height: 6px;
    border-radius: 50%; background: var(--gold);
  }
  .front-order {
    position: absolute; left: 34px; top: 560px; color: #fff; font-size: 9px; font-weight: 300;
  }
  .url-bar {
    position: absolute; background: var(--gold); color: var(--ink);
    font-weight: 600; font-size: 12px; padding: 6px 14px; white-space: nowrap;
  }
  .card--front .url-bar { left: 34px; top: 576px; }
  .front-floor {
    position: absolute; left: 0; bottom: 0; width: 100%; height: 110px;
    background: linear-gradient(180deg, #6b6e72 0%, #8e9195 100%);
  }

  /* back */
  .back-photo {
    position: absolute; left: 0; top: 0; width: 100%; height: 220px;
    background: linear-gradient(120deg, var(--room-b) 0%, var(--room-a) 45%, #3a4458 100%);
  }
  .card--back .title-box { right: 30px; top: 36px; font-size: 20px; }
  .card--back .tagline { left: 30px; top: 176px; font-size: 8.5px; }
  .back-order { position: absolute; right: 30px; top: 92px; color: #fff; font-size: 8px; font-weight: 300; text-align: right; }
  .card--back .url-bar { right: 30px; top: 106px; font-size: 11px; padding: 5px 12px; }
  .back-email { position: absolute; right: 30px; top: 136px; color: #fff; font-size: 8px; font-weight: 300; }

  .story {
    position: absolute; left: 28px; top: 238px; width: 464px; height: 390px;
    border: 2px solid var(--gold-line); padding: 18px 22px; background: #fff;
  }
  .story h2 { font-size: 14px; font-weight: 700; color: var(--ink); margin-bottom: 8px; }
  .story p { font-size: 9.4px; line-height: 1.5; color: var(--body); font-weight: 400; margin-bottom: 7px; }
  .story strong { color: var(--ink); font-weight: 700; }
  .story .closing { text-align: right; font-weight: 700; color: var(--ink); font-size: 10.5px; margin-top: 10px; margin-bottom: 0; }

  .phone {
    position: absolute; left: 28px; bottom: 34px; display: flex; align-items: center; gap: 8px;
    font-size: 20px; font-weight: 600; color: var(--ink);
  }
  .brand {
    position: absolute; right: 28px; bottom: 92px; display: flex; align-items: center; gap: 6px;
    font-size: 12px; font-weight: 600; color: var(--gold-line); text-transform: uppercase;
  }
  .brand-dot { width: 14px; height: 14px; border-radius: 50%; background: var(--gold-line); }
  .footer-note {
    position: absolute; right: 28px; bottom: 38px; width: 240px; text-align: right;
    font-size: 8px; line-height: 1.4; color: var(--body);
  }
</style>
</head>
<body>

<section class="card card--front" aria-label="Front of card">
  <div class="front-photo" role="img" aria-label="Photo of the sheepskin-lined Burrow Chair seen from above"></div>
  <p class="tagline"><b>HANDMADE</b> WITH LOVE AND DETAIL</p>
  <h1 class="title-box">Burrow Chair</h1>
  <div class="front-intro">
    <p>Burrow Chair is unique and a labor of love and attention to detail, it's a conversation starter or statement piece. It's something you just can't find anywhere.</p>
    <p>The acoustics let you escape in any room whether you want to read a book or simply relax.</p>
  </div>
  <ul class="feature-list">
    <li>Upholstered in<br>Italian Leather</li>
    <li>High Quality Merino<br>Wool Sheepskins</li>
    <li>360 Degree Rotation</li>
    <li>Cosy</li>
    <li>Calming</li>
    <li>Unbelievably<br>Quiet Acoustics</li>
    <li>Unique</li>
  </ul>
  <p class="front-order">Please order on our web site</p>
  <p class="url-bar">www.trvexports-example.com.au</p>
  <div class="front-floor" role="img" aria-label="Polished concrete floor of the lifestyle room"></div>
</section>

<section class="card card--back" aria-label="Back of card">
  <div class="back-photo" role="img" aria-label="Modern room with tall window and the Burrow Chair on a timber floor"></div>
  <h1 class="title-box">Burrow Chair</h1>
  <p class="back-order">Please order on our web site</p>
  <p class="url-bar">www.trvexports-example.com.au</p>
  <p class="back-email">or email sales@trvexp-example.com.au</p>
  <p class="tagline"><b>HANDMADE</b> WITH LOVE AND DETAIL</p>

  <article class="story">
    <h2>The Dome or Halo chair</h2>
    <p>When <strong>Tapio Lindqvist</strong> had the first idea for the <strong>Dome Chair in 1963</strong>, fibreglass was a relatively new material as glass reinforced products were not Batch Produced as they are today. The only possibility was to craft the chair with his own hands. It took Tapio and his brother in law nearly one year until the first prototype was ready.</p>
    <p>The prototype was a success, it is still standing in Tapios house. By coincidence two young product managers from the company VELNO discovered the Dome Chair when visiting Tapio in order to look at some pine wood chairs. They immediately realised the potential of this design icon.</p>
    <p>In 1966 for the first time the chair was presented at the Northern Interiors Expo in Cologne. Celebrities bought copies of the original for their homes and it found itself in a variety of Design Museums throughout the world.</p>
    <p>The design of the chair was not only striking to look at but it was also comfortable and relaxing to sit in for long periods of time. The chair has been described as "a room within a room". It offers shelter, a calming atmosphere and privacy for the seated person.</p>
    <p>Our Replica Tapio Lindqvist Dome chair is made to exacting standards. The shell is made from solid fiberglass, and is finished in Italian leather. The interior of the ball is padded and covered in lambswool merino sheepskins. The chair is available in different colours.</p>
    <p class="closing">We hope you love this product as much as we do<br>and have many years enjoyment in it</p>
  </article>

  <p class="brand"><span class="brand-dot"></span>TRV Exports</p>
  <p class="footer-note">Property of TRV Exports we love to create comfortable and unique things which people talk about and want to adorn their living spaces with.</p>

  <p class="phone">
    <svg width="20" height="20" viewBox="0 0 24 24" aria-hidden="true">
      <path d="M6.6 10.8a15.1 15.1 0 0 0 6.6 6.6l2.2-2.2a1 1 0 0 1 1-.25 11.4 11.4 0 0 0 3.6.57 1 1 0 0 1 1 1V20a1 1 0 0 1-1 1A17 17 0 0 1 3 4a1 1 0 0 1 1-1h3.5a1 1 0 0 1 1 1c0 1.25.2 2.45.57 3.57a1 1 0 0 1-.25 1z" fill="#e0b12a"/>
    </svg>
    0491 203 417
  </p>
</section>

</body>
</html>
```